landscaping core flute signs

I need core flutes created with business name and a few extra dot points for putting on fences for job sites 120cm x 120cm approx.
I want our old ones information with the new L logo and colour palette

```html
<!DOCTYPE html>
<html lang="en">
<head>
<meta charset="utf-8">
<title>Ridgeline Grounds – Site Sign</title>
<link href="https://fonts.googleapis.com/css2?family=Bebas+Neue&family=Cinzel:wght@600&family=Montserrat:wght@500;600;800&display=swap" rel="stylesheet">
<style>
  :root {
    --green: #65905a;
    --green-dark: #4e7442;
    --ink: #050507;
    --paper: #ffffff;
    --mist: #d4d4d5;
  }
  html, body {
    margin: 0;
    padding: 0;
    width: 1200px;
    height: 1200px;
    overflow: hidden;
  }
  .sign {
    position: relative;
    width: 1200px;
    height: 1200px;
    overflow: hidden;
    background: linear-gradient(180deg, var(--mist) 0%, var(--paper) 30%, var(--paper) 55%, #c9c8ca 76%);
    font-family: "Montserrat", sans-serif;
  }
  .chevron {
    position: absolute;
    inset: 0;
  }
  .licence {
    position: absolute;
    left: 52px;
    top: 59px;
    height: 31px;
    display: flex;
    align-items: stretch;
    border-radius: 16px;
    overflow: hidden;
    font-family: "Montserrat", sans-serif;
    font-weight: 600;
    font-size: 22px;
    letter-spacing: 1.5px;
    line-height: 31px;
  }
  .licence-label {
    background: var(--ink);
    color: var(--paper);
    padding: 0 8px 0 10px;
  }
  .licence-number {
    background: var(--green);
    color: var(--paper);
    padding: 0 10px 0 8px;
    border-radius: 16px 0 0 16px;
    margin-left: -4px;
  }
  .brand-mark {
    position: absolute;
    left: 451px;
    top: 54px;
    width: 298px;
    height: 298px;
    border-radius: 50%;
    background: var(--green);
  }
  .brand-name {
    position: absolute;
    left: 0;
    right: 0;
    top: 380px;
    margin: 0;
    text-align: center;
    font-family: "Cinzel", serif;
    font-weight: 600;
    color: var(--ink);
  }
  .brand-name .line-main {
    display: block;
    font-size: 94px;
    line-height: 92px;
    letter-spacing: 1px;
  }
  .brand-name .line-sub {
    display: flex;
    align-items: center;
    justify-content: center;
    gap: 26px;
    font-size: 50px;
    line-height: 52px;
    letter-spacing: 16px;
    margin-top: 2px;
  }
  .brand-name .rule {
    display: block;
    width: 144px;
    height: 3px;
    background: var(--ink);
    border-radius: 2px;
  }
  .tagline {
    position: absolute;
    left: 0;
    right: 0;
    top: 530px;
    margin: 0;
    text-align: center;
    font-family: "Cinzel", serif;
    font-weight: 600;
    font-size: 24px;
    letter-spacing: 10px;
    color: var(--green);
  }
  .services {
    position: absolute;
    top: 592px;
    left: 0;
    width: 1200px;
    margin: 0;
    padding: 0;
    list-style: none;
  }
  .service {
    position: absolute;
    top: 0;
    width: 340px;
    text-align: center;
    font-family: "Bebas Neue", sans-serif;
    font-size: 76px;
    line-height: 68px;
  }
  .service .top { display: block; color: var(--ink); }
  .service .bottom { display: block; color: var(--green); }
  .service.paving { left: 83px; }
  .service.fencing { left: 432px; }
  .service.design { left: 786px; }
  .divider {
    position: absolute;
    top: 587px;
    width: 4px;
    height: 162px;
  }
  .divider.one { left: 418px; }
  .divider.two { left: 782px; }
  .phone {
    position: absolute;
    left: 0;
    right: 0;
    top: 952px;
    margin: 0;
    text-align: center;
    font-family: "Montserrat", sans-serif;
    font-weight: 800;
    font-size: 128px;
    line-height: 128px;
    color: var(--paper);
    letter-spacing: 1px;
  }
  .email {
    position: absolute;
    left: 230px;
    top: 1081px;
    width: 725px;
    height: 68px;
    border-radius: 34px;
    background: var(--green);
    display: flex;
    align-items: center;
    justify-content: center;
    gap: 10px;
    color: var(--ink);
    font-family: "Montserrat", sans-serif;
    font-weight: 500;
    font-size: 40px;
    letter-spacing: 2.4px;
  }
  .email svg { flex: none; }
</style>
</head>
<body>
<main class="sign">
  <svg class="chevron" width="1200" height="1200" viewBox="0 0 1200 1200" aria-hidden="true">
    <polygon points="0,725 600,889 1200,725 1200,776 600,939 0,776" fill="var(--green)"/>
    <polygon points="600,889 1200,725 1200,776 690,914" fill="var(--green-dark)"/>
    <polygon points="0,776 600,939 1200,776 1200,1200 0,1200" fill="var(--ink)"/>
  </svg>

  <div class="licence">
    <span class="licence-label">QBSA</span>
    <span class="licence-number">1098421</span>
  </div>

  <div class="brand-mark" aria-hidden="true"></div>

  <h1 class="brand-name">
    <span class="line-main">RIDGELINE</span>
    <span class="line-sub"><span class="rule"></span>GROUNDS<span class="rule"></span></span>
  </h1>
  <p class="tagline">STRUCTURAL LANDSCAPING</p>

  <ul class="services">
    <li class="service paving"><span class="top">Paving &amp;</span><span class="bottom">Concreting</span></li>
    <li class="service fencing"><span class="top">Fencing</span><span class="bottom">&amp; Retaining</span></li>
    <li class="service design"><span class="top">Design &amp;</span><span class="bottom">Construct</span></li>
  </ul>

  <svg class="divider one" viewBox="0 0 4 162" aria-hidden="true">
    <path d="M2,0 Q4,81 2,162 Q0,81 2,0 Z" fill="var(--green)"/>
  </svg>
  <svg class="divider two" viewBox="0 0 4 162" aria-hidden="true">
    <path d="M2,0 Q4,81 2,162 Q0,81 2,0 Z" fill="var(--green)"/>
  </svg>

  <p class="phone">0491 570 156</p>

  <div class="email">
    <svg width="36" height="36" viewBox="0 0 36 36" aria-hidden="true">
      <rect x="2" y="14" width="32" height="20" fill="none" stroke="var(--ink)" stroke-width="2.5"/>
      <polyline points="2,14 18,26 34,14" fill="none" stroke="var(--ink)" stroke-width="2.5"/>
      <polyline points="2,34 14,23" fill="none" stroke="var(--ink)" stroke-width="2.5"/>
      <polyline points="34,34 22,23" fill="none" stroke="var(--ink)" stroke-width="2.5"/>
      <rect x="9" y="2" width="18" height="16" fill="var(--green)" stroke="var(--ink)" stroke-width="2.5"/>
      <text x="18" y="14" text-anchor="middle" font-family="Montserrat, sans-serif" font-size="10" font-weight="600" fill="var(--ink)">@</text>
    </svg>
    <span>sam@ridgelinegrounds.com</span>
  </div>
</main>
</body>
</html>
```